" A empresa terá uma atuação semelhante a Verdanex, Morvatel, Tribunex, Galvo Trimesta, IRVU, Qelmo, BREMU, DOVA e KUT. O propósito desta nova empresa é apoiar empresas na evolução dos seus negócios em suas camadas estratégica, tática e operacional direcionando-as para um mercado atual e futuro, e utilizando-se de conceitos, melhores práticas globais, tendencias, tecnologias modernas e profissionais especializados. "

```html
<!DOCTYPE html>
<html lang="pt-BR">
<head>
<meta charset="utf-8">
<title>Nuvora – Papelaria</title>
<link href="https://fonts.googleapis.com/css2?family=Montserrat:wght@400;500;600&display=swap" rel="stylesheet">
<style>
  :root {
    --bg: #ececec;
    --paper: #ffffff;
    --navy: #3c4150;
    --ink: #2f3442;
    --muted: #8a8f9c;
    --footer-text: #c9ccd4;
    --accent: #7a62b3;
    --rule: #5a6070;
  }
  * { box-sizing: border-box; margin: 0; padding: 0; }
  html, body { width: 1200px; height: 1200px; overflow: hidden; }
  body {
    background: var(--bg);
    font-family: "Montserrat", sans-serif;
    position: relative;
  }
  .letterhead {
    position: absolute; left: 60px; top: 225px;
    width: 480px; height: 679px;
    background: var(--paper);
    box-shadow: 0 6px 18px rgba(0,0,0,.12);
  }
  .envelope {
    position: absolute; left: 600px; top: 190px;
    width: 540px; height: 750px;
    background: var(--navy);
    box-shadow: 0 6px 18px rgba(0,0,0,.15);
    overflow: hidden;
  }
  .envelope-flap { position: absolute; left: 0; top: 0; width: 540px; height: 60px; }

  .brand { display: flex; flex-direction: column; gap: 5px; }
  .brand-row { display: flex; align-items: center; gap: 8px; }
  .brand-dot { width: 26px; height: 26px; border-radius: 50%; background: var(--accent); }
  .brand-name { font-weight: 600; font-size: 34px; letter-spacing: -0.5px; line-height: 1; color: var(--ink); }
  .brand-services {
    font-size: 5.5px; font-weight: 500; line-height: 1.25;
    letter-spacing: .6px; text-transform: uppercase; color: var(--muted);
    margin-left: 2px;
  }
  .brand-tagline {
    font-size: 7px; font-weight: 500; letter-spacing: 3.6px;
    text-transform: uppercase; color: var(--muted); margin-left: 2px;
    white-space: nowrap;
  }
  .letterhead .brand { position: absolute; left: 36px; top: 34px; }

  .envelope .brand { position: absolute; right: 34px; top: 600px; }
  .envelope .brand-name { color: #fff; }
  .envelope .brand-services, .envelope .brand-tagline { color: var(--footer-text); }

  .envelope-footer {
    position: absolute; left: 0; right: 0; bottom: 0; height: 62px;
    border-top: 1px solid var(--rule);
    display: grid; grid-template-columns: 1.6fr 1fr 1fr;
    gap: 14px; padding: 12px 22px 0;
    font-size: 7.5px; line-height: 1.6; color: var(--footer-text);
  }
  .footer-label { color: #fff; font-weight: 600; margin-right: 4px; }
  .social { display: flex; gap: 5px; margin-top: 4px; }
  .social span { width: 10px; height: 10px; border-radius: 50%; background: var(--footer-text); }
</style>
</head>
<body>

  <section class="letterhead" aria-label="Papel timbrado">
    <div class="brand">
      <div class="brand-row">
        <span class="brand-dot"></span>
        <span class="brand-name">nuvora</span>
        <span class="brand-services">Gestão<br>Tecnologia<br>Outsourcing</span>
      </div>
      <span class="brand-tagline">Shape the next step</span>
    </div>
  </section>

  <section class="envelope" aria-label="Envelope">
    <svg class="envelope-flap" viewBox="0 0 540 60" preserveAspectRatio="none">
      <polygon points="0,0 540,0 540,22 0,48" fill="#ffffff"/>
    </svg>

    <div class="brand">
      <div class="brand-row">
        <span class="brand-dot"></span>
        <span class="brand-name">nuvora</span>
        <span class="brand-services">Gestão<br>Tecnologia<br>Outsourcing</span>
      </div>
      <span class="brand-tagline">Shape the next step</span>
    </div>

    <footer class="envelope-footer">
      <div>
        <span class="footer-label">Address</span>Av Solano Pires, 1420<br>
        Conj 118 - São Paulo - 01230-010
      </div>
      <div>
        <span class="footer-label">Phone</span>(11) 4000-1234<br>
        <span class="footer-label">e-mail</span>contato@nuvora.com.br
      </div>
      <div>
        <span class="footer-label">Website</span>www.nuvora.com.br
        <div class="social" aria-hidden="true"><span></span><span></span><span></span><span></span><span></span></div>
      </div>
    </footer>
  </section>

</body>
</html>
```